Combining web page

We need a PSD webpage design for our PrestaShop store that shows food combining rules, you can see an example that we put here, you can follow the same information and food image combinations. You are just doing the design but the images when implemented on the website will be clickable that goes to product categories, all text and images will be editable.

This is just an example:
http://merrowtonic.com/content/7-food-combining-rules

Target Market(s)

Natural Product and supplement industry

Industry/Entity Type

Store

Number of Pages Required

1 page

Colors

Designer to choose colors to be used in the design.

Requirements
Must have
• 1. Clear images.
• 2. Clear readable text.
• 3. Company name shown Merrow Tonic.
• 4. Follow the food rules as seen on the web page example, but not the same design.
• 5. Logo should be seen.
• 7. All text and images will be editable.
• 8. Make sure the food images are in their proper groups.
• 9. You are not coping the design we gave you but the details have to be the same, copy the text and the image food groups are important, you cannot just put any food in a group, and the combinations are important.
Nice to have
• Here is the website it is for http://merrowtonic.com/

```html
<!DOCTYPE html>
<html lang="en">
<head>
<meta charset="utf-8">
<title>Food Combining Rules – Merrow Tonic</title>
<link href="https://fonts.googleapis.com/css2?family=Merriweather:wght@400;700&family=Lora:wght@400;700&family=Arimo:wght@400;700&display=swap" rel="stylesheet">
<style>
:root{
  --bg:#ebebeb;
  --paper:#ffffff;
  --ink:#1a1a1a;
  --muted:#555555;
  --black:#0e0e0e;
  --green:#6fae3a;
  --green-dark:#3f7d1f;
  --olive:#8aa14a;
  --line:#c9c9c9;
  --rule:#b5b5b5;
  --price:#7aa83f;
  --old:#888888;
}
*{box-sizing:border-box;margin:0;padding:0}
html,body{width:1200px;height:3010px;overflow:hidden}
body{background:var(--bg);font-family:"Lora",Georgia,serif;color:var(--ink);position:relative}
.abs{position:absolute}

/* decorations */
.leaf{position:absolute;border-radius:50%}
.fruit{position:absolute}

/* header */
.header{position:absolute;left:80px;top:0;width:1040px;height:238px;background:linear-gradient(#fbfbf9,#f1f0ec);border-bottom:4px solid #ddd9cf;box-shadow:0 3px 6px rgba(0,0,0,.12)}
.tagline{position:absolute;top:52px;left:0;width:100%;text-align:center;font-family:"Merriweather",serif;font-size:12px;letter-spacing:1px;font-weight:700;color:#333}
.search{position:absolute;left:90px;top:96px;width:210px;height:26px;border-bottom:1px solid #999;font-size:12px;color:#999;font-style:italic;padding-top:4px}
.search svg{position:absolute;right:2px;top:2px}
.brand{position:absolute;left:50%;top:86px;transform:translateX(-50%);display:flex;align-items:center;gap:8px}
.brand-mark{width:22px;height:22px;background:var(--green)}
.brand-name{font-family:"Merriweather",serif;font-weight:700;font-size:30px;color:var(--green-dark)}
.brand-sub{position:absolute;top:138px;left:0;width:100%;text-align:center;font-size:9px;color:#555}
.login{position:absolute;right:138px;top:52px;font-size:13px;font-family:"Merriweather",serif;color:#333}
.cart{position:absolute;right:110px;top:102px;font-size:15px;color:var(--green);display:flex;align-items:center;gap:8px}
.nav{position:absolute;top:186px;left:0;width:100%;display:flex;justify-content:center;gap:54px;font-family:"Merriweather",serif;font-size:13px;letter-spacing:.6px;color:#333}

.breadcrumb{position:absolute;top:272px;width:100%;text-align:center;font-size:12px;color:#555}
.breadcrumb b{font-weight:400;color:#333}

/* main */
.main{position:absolute;left:88px;top:300px;width:1022px;height:2330px;background:var(--paper)}

/* sidebar */
.side{position:absolute;left:26px;top:32px;width:230px}
.bar{background:var(--black);color:#fff;font-family:"Merriweather",serif;font-size:13px;height:34px;line-height:34px;padding-left:16px;font-weight:700}
.catlist{list-style:none;padding:16px 4px 0 4px;font-size:12.5px;font-family:"Merriweather",serif}
.catlist li{height:25px;display:flex;justify-content:space-between;color:#333}
.side-banner{margin-top:34px;width:230px;height:212px;background:radial-gradient(circle at 50% 45%,#d8a25b,#f3e7d4 55%,#fbfaf6);border:1px solid #eee}
.prod{display:flex;gap:12px;height:95px;padding-top:18px}
.thumb{width:70px;height:70px;border:1px solid #e3e3e3;flex:none;display:flex;align-items:center;justify-content:center}
.thumb i{display:block;width:42px;height:42px;border-radius:50%}
.prod-name{font-size:12.5px;line-height:18px;color:#222}
.price{font-size:12.5px;margin-top:8px;color:var(--price)}
.price s{color:var(--old);margin-left:4px}
.price em{font-style:normal;color:var(--old);margin-left:6px;font-size:11px}
.btn{display:block;width:108px;height:30px;margin:14px 4px 0 auto;border-radius:15px;background:#2a2a2a;color:#fff;font-size:12px;text-align:center;line-height:30px;font-family:"Merriweather",serif;box-shadow:0 2px 0 #000}

/* content */
.content{position:absolute;left:274px;top:30px;width:720px}
.page-title{font-family:"Merriweather",serif;font-weight:700;font-size:17px;color:#111}
.group-box{margin-top:14px;border:1px solid #e2e2e2;height:560px;position:relative}
.group-head{position:absolute;left:20px;top:14px;width:680px;height:38px;border-top:1px solid #999;border-bottom:1px solid #999;background:linear-gradient(#fafafa,#eee);text-align:center;line-height:36px;font-family:"Merriweather",serif;font-size:15px}
.tile{position:absolute;width:162px;text-align:center}
.tile-img{width:128px;height:80px;margin:0 auto;border:1px solid #cfcfcf;box-shadow:0 2px 4px rgba(0,0,0,.15);background:#fff;display:flex;align-items:center;justify-content:center}
.tile-img i{display:block;width:90px;height:56px;border-radius:40%}
.tile-label{margin-top:14px;height:34px;line-height:32px;border:1px solid #cfcfcf;box-shadow:0 2px 3px rgba(0,0,0,.15);font-family:"Arimo",sans-serif;font-size:13px;color:#333;white-space:nowrap;overflow:hidden;text-overflow:ellipsis;padding:0 6px}

.easy-bar{position:relative;margin-top:8px;height:52px;background:var(--black);color:#fff;text-align:center;line-height:52px;font-family:"Merriweather",serif;font-size:15px}
.easy-bar .ivy{position:absolute;top:-8px;width:70px;height:62px;background:radial-gradient(circle,#7fae47,#4c7d2a 60%,transparent 70%);border-radius:50%}
.classified{font-family:"Merriweather",serif;font-size:12px;margin:6px 0 6px 12px}

/* table */
.rules{margin-left:26px;width:688px;border-collapse:collapse;table-layout:fixed;font-family:"Arimo",sans-serif}
.rules td,.rules th{border:1px solid var(--rule);vertical-align:middle;text-align:center;font-weight:400}
.rules col.lbl{width:312px}
.rules thead th{height:120px;vertical-align:top;font-size:11px;line-height:13px;padding-top:4px}
.rules thead th .n{display:block;font-size:13px;margin-bottom:8px}
.key{text-align:left!important;padding:6px 8px;font-size:11.5px!important;line-height:16px!important}
.key div{display:flex;gap:14px}
.rowlbl{position:relative;text-align:right!important;padding:4px 36px 4px 8px;font-size:11.5px}
.rowlbl h3{font-family:"Arimo",sans-serif;font-size:14px;font-weight:700;margin-bottom:6px}
.rowlbl .grid{display:grid;grid-template-columns:repeat(3,72px);justify-content:end;column-gap:4px;font-size:11px;line-height:15px;text-align:left;font-family:"Lora",serif}
.rowlbl .num{position:absolute;right:10px;top:50%;transform:translateY(-30%);font-size:30px;font-family:"Arimo",sans-serif}
.cell{font-size:14px}
.cell small{display:block;font-size:10px;line-height:12px}

.principles{text-align:center;font-family:"Merriweather",serif;font-size:15px;margin-top:28px}
.pcols{display:grid;grid-template-columns:repeat(4,1fr);gap:24px;padding:22px 24px 0 36px;font-size:11px;line-height:15px;word-break:break-all}

/* footer */
.footer{position:absolute;left:0;top:2640px;width:1200px;height:370px;background:linear-gradient(#f3f2ee,#e9e7e0)}
.social{position:absolute;top:72px;left:0;width:100%;display:flex;justify-content:center;gap:12px}
.social span{width:24px;height:24px;border-radius:50%;background:#111}
.flinks{position:absolute;top:118px;left:0;width:100%;text-align:center;font-size:12.5px;line-height:22px;color:#222;font-family:"Lora",serif}
.flinks span{margin:0 8px}
.subscribe{position:absolute;left:438px;top:182px;width:322px;height:36px;border:1px solid #aaa;border-radius:18px;background:#fff;overflow:hidden}
.subscribe b{position:absolute;right:0;top:0;height:36px;width:108px;background:#111;color:#fff;font-weight:400;font-size:12px;line-height:36px;text-align:center;font-family:"Merriweather",serif;border-radius:0 18px 18px 0}
.fnote{position:absolute;top:236px;left:0;width:100%;text-align:center;font-size:11.5px;line-height:20px;color:var(--price)}
.copy{position:absolute;top:292px;left:0;width:100%;text-align:center;font-size:12.5px;color:#222}
.to-top{position:absolute;left:1130px;top:2914px;width:32px;height:32px;border-radius:50%;background:var(--green)}
</style>
</head>
<body>

<!-- side decorations -->
<div class="fruit" style="left:0;top:320px;width:100px;height:480px;background:radial-gradient(ellipse at 20% 45%,#f7d23a,#f0b51d 45%,#9cc94a 70%,transparent 72%)" role="img" aria-label="Lemon slices and green leaves"></div>
<div class="fruit" style="left:1110px;top:820px;width:90px;height:460px;background:radial-gradient(ellipse at 90% 50%,#f7a11f,#e4572a 45%,#8fb34a 68%,transparent 72%)" role="img" aria-label="Ripe mango halves"></div>
<div class="fruit" style="left:0;top:1530px;width:90px;height:430px;background:radial-gradient(ellipse at 10% 50%,#cfe3a6,#8fbf5a 50%,#5d8e35 68%,transparent 72%)" role="img" aria-label="Green cabbage head"></div>
<div class="fruit" style="left:1110px;top:2080px;width:90px;height:660px;background:radial-gradient(ellipse at 90% 45%,#ffb12e,#f07a14 40%,#d43a2a 60%,transparent 70%)" role="img" aria-label="Orange and fruit slices with juice splash"></div>

<header class="header">
  <div class="abs" style="left:-30px;top:0;width:150px;height:230px;background:radial-gradient(ellipse at 30% 30%,#6fa63a,#3d7a1f 55%,transparent 70%)" role="img" aria-label="Hanging ivy leaves"></div>
  <div class="abs" style="right:-30px;top:0;width:150px;height:230px;background:radial-gradient(ellipse at 70% 30%,#6fa63a,#3d7a1f 55%,transparent 70%)" role="img" aria-label="Hanging ivy leaves"></div>
  <div class="tagline">ANCIENT FOODS FOR TODAYS LIFESTYLE</div>
  <div class="search">Search
    <svg width="18" height="18" viewBox="0 0 18 18"><circle cx="7.5" cy="7.5" r="5.5" fill="none" stroke="#333" stroke-width="1.6"/><line x1="11.5" y1="11.5" x2="16" y2="16" stroke="#333" stroke-width="1.8"/></svg>
  </div>
  <div class="brand"><span class="brand-mark"></span><span class="brand-name">Merrow Tonic</span></div>
  <div class="brand-sub">Ancient Foods for Today's People</div>
  <div class="login">Login ⌄</div>
  <div class="cart">
    <svg width="22" height="20" viewBox="0 0 22 20"><path d="M1 2h4l3 11h10l3-8H7" fill="none" stroke="#555" stroke-width="1.6"/><circle cx="9" cy="17" r="1.6" fill="#555"/><circle cx="17" cy="17" r="1.6" fill="#555"/></svg>
    (0 Cart)
  </div>
  <nav class="nav"><span>OUR PRODUCTS</span><span>INGREDIENTS</span><span>HEALTH CONCERNS</span><span>OUR BLOGS</span><span>MORE</span></nav>
</header>

<div class="breadcrumb"><b>Home</b> &nbsp;|&nbsp; Food Combining Rules</div>

<main class="main">
  <aside class="side">
    <div class="bar">Home</div>
    <ul class="catlist">
      <li>Our Products<span>+</span></li>
      <li>Ingredients<span>+</span></li>
      <li>Health Concerns</li>
      <li>Edible Legumes</li>
      <li>Asparagus</li>
      <li>Cauliflower</li>
      <li>Cabbages<span>+</span></li>
    </ul>
    <div class="side-banner" role="img" aria-label="Wicker basket of fresh vegetables, captioned Fresh vegetables"></div>

    <div class="bar" style="margin-top:88px">Best Sellers</div>
    <div class="prod"><div class="thumb"><i style="background:#e98b2a"></i></div><div><div class="prod-name">The Adventure Begins Framed...</div><div class="price">$29.00</div></div></div>
    <div class="prod"><div class="thumb"><i style="background:#d84a2a"></i></div><div><div class="prod-name">Mountain Fox Notebook</div><div class="price">$12.90</div></div></div>
    <div class="prod"><div class="thumb"><i style="background:#f2c43a"></i></div><div><div class="prod-name">Wrenfield Printed Sweater</div><div class="price">$28.72<s>$35.90</s><em>-20%</em></div></div></div>
    <span class="btn">All Products</span>

    <div class="bar" style="margin-top:44px">Featured Products</div>
    <div class="prod"><div class="thumb"><i style="background:#b8d36a"></i></div><div><div class="prod-name">Wrenfield Printed T-shirt</div><div class="price">$19.12<s>$23.90</s><em>-20%</em></div></div></div>
    <div class="prod"><div class="thumb"><i style="background:#f2c43a"></i></div><div><div class="prod-name">Wrenfield Printed Sweater</div><div class="price">$28.72<s>$35.90</s><em>-20%</em></div></div></div>
    <div class="prod"><div class="thumb"><i style="background:#e98b2a"></i></div><div><div class="prod-name">The Best Is Yet To Come'...</div><div class="price">$29.00</div></div></div>
    <span class="btn">All Products</span>

    <div class="bar" style="margin-top:44px">New Products</div>
    <div class="prod"><div class="thumb"><i style="background:#d9663a"></i></div><div><div class="prod-name">Customizable Mug</div><div class="price">$13.69<s>$13.90</s><em>-2%</em></div></div></div>
    <div class="prod"><div class="thumb"><i style="background:#7fb33f"></i></div><div><div class="prod-name">Wrenfield Notebook</div><div class="price">$12.75<s>$12.90</s><em>-1%</em></div></div></div>
    <div class="prod"><div class="thumb"><i style="background:#8cc05a"></i></div><div><div class="prod-name">Brown Bear Notebook</div><div class="price">$12.64<s>$12.90</s><em>-2%</em></div></div></div>
    <span class="btn">All Products</span>

    <div class="bar" style="margin-top:44px">Special Products</div>
    <div class="prod"><div class="thumb"><i style="background:#f2c43a"></i></div><div><div class="prod-name">Wrenfield Printed Sweater</div><div class="price">$28.72<s>$35.90</s><em>-20%</em></div></div></div>
    <div class="prod"><div class="thumb"><i style="background:#b8d36a"></i></div><div><div class="prod-name">Wrenfield Printed T-shirt</div><div class="price">$19.12<s>$23.90</s><em>-20%</em></div></div></div>
    <div class="prod"><div class="thumb"><i style="background:#d9663a"></i></div><div><div class="prod-name">Customizable Mug</div><div class="price">$13.69<s>$13.90</s><em>-2%</em></div></div></div>
    <span class="btn">All Products</span>
  </aside>

  <section class="content">
    <h1 class="page-title">Food Combining Rules</h1>
    <div class="group-box">
      <div class="group-head">Merrow Tonic</div>
      <a class="tile" style="left:26px;top:80px"><div class="tile-img"><i style="background:radial-gradient(#ffb43a,#f07d12)" role="img" aria-label="Oranges"></i></div><div class="tile-label">Citrus - Acid Fruits</div></a>
      <a class="tile" style="left:278px;top:80px"><div class="tile-img"><i style="background:radial-gradient(#e5503a,#7a9b3a)" role="img" aria-label="Mixed sub-acid fruits"></i></div><div class="tile-label">Fruits (Sub-Acid)</div></a>
      <a class="tile" style="left:534px;top:80px"><div class="tile-img"><i style="background:radial-gradient(#f5d24a,#c9962a)" role="img" aria-label="Pineapple and sweet fruits"></i></div><div class="tile-label">Sweet Fruits - Palm Fruits</div></a>
      <a class="tile" style="left:26px;top:250px"><div class="tile-img"><i style="background:radial-gradient(#c99a62,#7e5530)" role="img" aria-label="Raw nuts and seeds"></i></div><div class="tile-label">Neutral Fruits-Raw Nut...</div></a>
      <a class="tile" style="left:278px;top:250px"><div class="tile-img"><i style="background:radial-gradient(#d9b882,#a07a45)" role="img" aria-label="Sack of grains"></i></div><div class="tile-label">Grains</div></a>
      <a class="tile" style="left:534px;top:250px"><div class="tile-img"><i style="background:radial-gradient(#b8743a,#6e3f22)" role="img" aria-label="Dried legumes and sprouts"></i></div><div class="tile-label">Legumes - Sprouts</div></a>
      <a class="tile" style="left:26px;top:420px"><div class="tile-img"><i style="background:radial-gradient(#f0a35a,#6d9a3a)" role="img" aria-label="Melons"></i></div><div class="tile-label">Melons</div></a>
      <a class="tile" style="left:278px;top:420px"><div class="tile-img"><i style="background:radial-gradient(#e0452e,#5e9a32)" role="img" aria-label="Tomatoes and succulent foods"></i></div><div class="tile-label">Succulent Foods...</div></a>
      <a class="tile" style="left:534px;top:420px"><div class="tile-img"><i style="background:radial-gradient(#8cc04a,#d8702a)" role="img" aria-label="Basket of vegetables"></i></div><div class="tile-label">Vegetables</div></a>
    </div>

    <div class="easy-bar">
      <span class="ivy" style="left:-14px" role="img" aria-label="Ivy leaves"></span>
      <span class="ivy" style="right:-14px" role="img" aria-label="Ivy leaves"></span>
      Food Combining Made Easy
    </div>
    <div class="classified">Natural Feeds Food - Classified</div>

    <table class="rules">
      <colgroup><col class="lbl"><col><col><col><col><col><col><col><col><col></colgroup>
      <thead>
        <tr>
          <th class="key"><div><span>Key :</span><span>xx Combines Well<br>x Fair Compatibility</span><span>Nr Not Recommended<br>No Not Compatible</span></div></th>
          <th><span class="n">1</span>Citrus Acid Fruits</th>
          <th><span class="n">2</span>Fruits (Sub-Acid)</th>
          <th><span class="n">3</span>Sweet Fruits-Palm Fruits</th>
          <th><span class="n">4</span>Neutr-al Fruit s-Palm Fruits</th>
          <th><span class="n">5</span>Grains</th>
          <th><span class="n">6</span>Legu-Mes-Sprou-ts</th>
          <th><span class="n">7</span>Melo-ns</th>
          <th><span class="n">8</span>Succ-ulent Foods-Tomat oes</th>
          <th><span class="n">9</span>Vegi-tables</th>
        </tr>
      </thead>
      <tbody>
        <tr style="height:113px">
          <td class="rowlbl"><h3>CITRUS - ACID FRUITS</h3><div class="grid"><span>Lorem Ipsum</span><span>Orange</span><span>Orange</span><span>Lorem Ipsum</span><span>Orange</span><span>Orange</span><span>Lorem Ipsum</span><span>Orange</span><span>Orange</span><span>Lorem Ipsum</span></div><span class="num">1</span></td>
          <td class="cell">XX</td><td class="cell">XX</td><td class="cell"><small>xx text<br>xx text<br>xx text</small>XX</td><td class="cell">XX</td><td class="cell">NR<small>xx text<br>xx text</small></td><td class="cell">X-NR<small>xx text<br>xx text</small></td><td class="cell">X</td><td class="cell">XX<small>xx text</small></td><td class="cell">NO<small>xx text</small></td>
        </tr>
        <tr style="height:120px">
          <td class="rowlbl"><h3 style="font-weight:400">FRUITS ( Sub-Acid)</h3><div class="grid" style="grid-template-columns:repeat(4,54px)"><span>Orange</span><span>Orange</span><span>Orange</span><span>Orange</span><span>Orange</span><span>Orange</span><span>Orange</span><span>Orange</span><span>Orange</span><span>Orange</span><span>Orange</span><span>Orange</span><span>Orange</span><span>Orange</span><span>Orange</span><span>Orange</span></div><span class="num">2</span></td>
          <td class="cell">XX</td><td class="cell">XX</td><td class="cell">XX</td><td class="cell">XX</td><td class="cell">NR<small>xx text<br>xx text</small></td><td class="cell">X<small>xx text<br>xx text</small></td><td class="cell">X</td><td class="cell">NO</td><td class="cell">NO</td>
        </tr>
        <tr style="height:118px">
          <td class="rowlbl"><h3>SWEET FRUITS - PALM FRUITS</h3><div class="grid"><span>Lorem Ipsum</span><span>Orange</span><span>Orange</span><span>Lorem Ipsum</span><span>Orange</span><span>Orange</span><span>Lorem Ipsum</span><span>Orange</span><span>Orange</span><span>Lorem Ipsum</span><span>Orange</span><span>Orange</span></div><span class="num">3</span></td>
          <td class="cell"><small>xx text</small>XX<small>xx text<br>xx text</small></td><td class="cell">XX</td><td class="cell">XX</td><td class="cell">XX</td><td class="cell">XX</td><td class="cell"><small>xx text</small>X-NR<small>xx text<br>xx text<br>xx text</small></td><td class="cell">X-NR</td><td class="cell"></td><td class="cell">NO<small>xx text<br>xx text<br>xx text</small></td>
        </tr>
        <tr style="height:116px">
          <td class="rowlbl"><h3>NEUTRAL FRUITS- RAW NUTS-SEEDS</h3><div class="grid" style="grid-template-columns:repeat(4,54px)"><span>Orange</span><span>Orange</span><span>Orange</span><span>Orange</span><span>Orange</span><span>Orange</span><span>Orange</span><span>Orange</span><span>Orange</span><span>Orange</span><span>Orange</span><span>Orange</span><span></span><span>Orange</span><span>Orange</span><span>Orange</span></div><span class="num">4</span></td>
          <td class="cell">XX</td><td class="cell">XX</td><td class="cell">XX</td><td class="cell">XX</td><td class="cell">XX</td><td class="cell">XX</td><td class="cell">X</td><td class="cell">XX</td><td class="cell">XX</td>
        </tr>
        <tr style="height:118px">
          <td class="rowlbl"><h3>GRAINS</h3><div class="grid"><span>Lorem Ipsum</span><span>Orange</span><span>Orange</span><span>Lorem Ipsum</span><span>Orange</span><span>Orange</span><span>Lorem Ipsum</span><span>Orange</span><span>Orange</span><span>Lorem Ipsum</span><span>Orange</span><span>Orange</span></div><span class="num">5</span></td>
          <td class="cell"><small>xx text<br>xx text</small>XX</td><td class="cell">XX</td><td class="cell">XX</td><td class="cell">XX</td><td class="cell">XX</td><td class="cell">XX</td><td class="cell">X-NR</td><td class="cell">XX</td><td class="cell">XX</td>
        </tr>
        <tr style="height:132px">
          <td class="rowlbl"><h3>Legumes(dry) - SPROUTS</h3><div class="grid" style="grid-template-columns:repeat(4,54px)"><span>Orange</span><span>Orange</span><span>Orange</span><span>Orange</span><span>Orange</span><span>Orange</span><span>Orange</span><span>Orange</span><span>Orange</span><span>Orange</span><span>Orange</span><span>Orange</span><span>Orange</span><span>Orange</span><span>Orange</span><span>Orange</span></div><span class="num">6</span></td>
          <td class="cell">XX</td><td class="cell"><small>xx text<br>xx text</small>XX</td><td class="cell"><small>xx text<br>xx text<br>xx text</small>XX<small>xx text</small></td><td class="cell">XX</td><td class="cell">XX</td><td class="cell">XX</td><td class="cell">NR</td><td class="cell">XX</td><td class="cell"><small>xx text</small>XX</td>
        </tr>
        <tr style="height:116px">
          <td class="rowlbl"><h3>MELONS</h3><div class="grid"><span>Lorem Ipsum</span><span>Orange</span><span>Orange</span><span>Lorem Ipsum</span><span>Orange</span><span>Orange</span><span>Lorem Ipsum</span><span>Orange</span><span>Orange</span><span></span><span></span><span>Orange</span></div><span class="num">7</span></td>
          <td class="cell">XX</td><td class="cell"><small>xx text<br>xx text</small>XX</td><td class="cell">X-NR</td><td class="cell">X</td><td class="cell">NR</td><td class="cell">NR</td><td class="cell">XX</td><td class="cell">NR</td><td class="cell">NO</td>
        </tr>
        <tr style="height:202px">
          <td class="rowlbl"><h3>SUCCULENT FOODS - TOMATOES</h3><div class="grid"><span>Orange</span><span>Orange</span><span>Orange Orange</span><span>Orange</span><span>Orange</span><span>Orange Orange</span><span>Orange</span><span>Orange</span><span>Orange Orange</span><span>Orange</span><span>Orange</span><span>Orange Orange</span><span>Orange</span><span>Orange</span><span>Orange Orange</span><span></span><span>Orange</span><span>Orange Orange</span><span></span><span></span><span>Orange Orange</span><span></span><span></span><span>Orange Orange</span><span></span><span></span><span>Orange</span></div><span class="num">8</span></td>
          <td class="cell"><small>xx text</small>No</td><td class="cell">No</td><td class="cell">No</td><td class="cell">XX</td><td class="cell">XX</td><td class="cell">XX</td><td class="cell">NR</td><td class="cell">XX</td><td class="cell"><small>xx text</small>XX<small>xx text</small></td>
        </tr>
        <tr style="height:215px">
          <td class="rowlbl"><h3>SUCCULENT FOODS - TOMATOES</h3><div class="grid" style="grid-template-columns:28px 48px 48px 48px 48px"><span>text</span><span>Orange</span><span>Orange</span><span>Orange</span><span>Orange</span><span>text</span><span>Orange</span><span>Orange</span><span>Orange</span><span>Orange</span><span>text</span><span>Orange</span><span>Orange</span><span>Orange</span><span>Orange</span><span>text</span><span>Orange</span><span>Orange</span><span>Orange</span><span>Orange</span><span>text</span><span>Orange</span><span>Orange</span><span>Orange</span><span>Orange</span><span>text</span><span>Orange</span><span>Orange</span><span>Orange</span><span>Orange</span><span>text</span><span>Orange</span><span>Orange</span><span>Orange</span><span>Orange</span><span>text</span><span>Orange</span><span>Orange</span><span>Orange</span><span>Orange</span></div><span class="num" style="top:30px;transform:none">9</span></td>
          <td class="cell"><small>xx text</small>No</td><td class="cell">No</td><td class="cell"><small>xx text<br>xx text</small>No<small>xx text</small></td><td class="cell">XX</td><td class="cell">XX</td><td class="cell">XX<small>xx text</small></td><td class="cell">NR</td><td class="cell">XX<small>xx text</small></td><td class="cell">XX</td>
        </tr>
      </tbody>
    </table>

    <h2 class="principles">Principles of Eating</h2>
    <div class="pcols">
      <p>Eat fruit alone and on an empty stomach.Keep melons apart from other foods.Pair greens with grains or proteins for easy digestion.</p>
      <p>Combine starches with vegetables,never with acid fruits.Wait two hours between meals.Chew slowly and drink water before eating,not during.</p>
      <p>Proteins digest best with leafy greens.Avoid mixing two concentrated proteins.Sprouted legumes are lighter than dry ones on the stomach.</p>
      <p>Raw nuts and seeds suit sweet or acid fruits.Tomatoes pair with greens and nuts.Listen to your body and adjust each meal to suit it.</p>
    </div>
  </section>
</main>

<footer class="footer">
  <div class="abs" style="left:20px;top:0;width:170px;height:370px;background:radial-gradient(ellipse at 40% 50%,#7aae43,#4d8526 50%,transparent 70%)" role="img" aria-label="Climbing ivy vines"></div>
  <div class="abs" style="right:20px;top:0;width:170px;height:370px;background:radial-gradient(ellipse at 60% 50%,#7aae43,#4d8526 50%,transparent 70%)" role="img" aria-label="Climbing ivy vines"></div>
  <div class="social"><span></span><span></span><span></span></div>
  <div class="flinks">
    <span>Delivery</span>|<span>Legal Notice</span>|<span>Terms And Conditions Of Use</span>|<span>About Us</span>|<span>Secure Payment</span>|<span>Food Combining Rules</span><span>LARK COMBINING</span><br>
    |<span>Lark CSS CODE</span>|<span>Contact Us</span>|<span>Sitemap</span>|<span>Stores</span>
  </div>
  <div class="subscribe"><b>SUBSCRIBE</b></div>
  <div class="fnote">You May Unsubscribe At Any Moment. For That Purpose,<br>Please Find Our Contact Info In The Legal Notice.</div>
  <div class="copy">© 2017 Ecommerce site powered by Leafcraft</div>
</footer>
<div class="to-top">
  <svg width="32" height="32" viewBox="0 0 32 32"><path d="M10 19l6-6 6 6" fill="none" stroke="#fff" stroke-width="2"/></svg>
</div>

</body>
</html>
```